Stationary & Business Card for a Rock climbing company based primarily in Joshua Tree NP
Use provided logo
Stationary & Business Card for a Rock climbing company based primarily in Joshua Tree NP - Outdoors
Creative Brief
Simple
Garrick Fenn
Director
27615 Marrow Lane Victorville, CA 92307
garrickfenn@mailbrook.com
www.ridgepathoutfitters.com

```html
<!DOCTYPE html>
<html lang="en">
<head>
<meta charset="utf-8">
<title>Ridgepath Outfitters – Stationery</title>
<link rel="stylesheet" href="https://fonts.googleapis.com/css2?family=Open+Sans:wght@400;600;700&display=swap">
<style>
:root{
  --brown:#3e2c27;
  --orange:#f2952b;
  --paper:#ffffff;
  --stage:#f1f0ee;
  --ink:#6a625f;
  --muted:#a9a4a2;
  --ghost:#e4e2e0;
}
*{box-sizing:border-box;margin:0;padding:0}
html,body{width:1200px;height:936px;overflow:hidden}
body{background:var(--stage);font-family:"Open Sans",Arial,sans-serif;color:var(--ink);position:relative}
.sheet{position:absolute;background:var(--paper);box-shadow:0 2px 8px rgba(0,0,0,.18)}
.brand{display:flex;align-items:center;gap:8px}
.brand-dot{border-radius:50%;background:var(--orange);flex:none}
.brand-name{font-weight:700;text-transform:uppercase;letter-spacing:.06em;line-height:1.1}

/* letterhead */
.letterhead{left:46px;top:13px;width:393px;height:612px;padding:26px 30px}
.letterhead .brand-dot{width:44px;height:44px}
.letterhead .brand-name{font-size:10px;color:var(--brown)}
.lh-contact{position:absolute;right:30px;top:30px;font-size:5.5px;line-height:1.7;color:var(--muted)}
.lh-body{margin-top:46px;font-size:6px;line-height:1.8;color:var(--ink)}
.lh-body p{margin-bottom:10px}
.lh-sign{margin:6px 0 4px;width:44px;height:14px;border-bottom:1px solid var(--ink)}
.lh-footer{position:absolute;left:0;right:0;bottom:28px;text-align:center;font-size:6px;letter-spacing:.25em;color:var(--ink);text-transform:uppercase}

/* folder */
.folder{left:454px;top:13px;width:690px;height:612px;background:var(--brown)}
.folder .brand{position:absolute;left:0;right:0;top:200px;flex-direction:column;gap:16px}
.folder .brand-dot{width:130px;height:130px}
.folder .brand-name{font-size:26px;color:var(--orange);text-align:center}
.folder-web{position:absolute;left:0;right:0;bottom:44px;text-align:center;font-size:11px;letter-spacing:.3em;color:var(--orange);text-transform:uppercase}

/* business cards */
.card{left:46px;width:154px;height:102px}
.card-front{top:664px;padding:12px}
.card-front .brand{position:absolute;left:10px;top:14px;flex-direction:column;gap:4px;width:58px}
.card-front .brand-dot{width:30px;height:30px}
.card-front .brand-name{font-size:5.5px;color:var(--brown);text-align:center}
.card-info{position:absolute;left:76px;top:14px;font-size:4.6px;line-height:1.7;color:var(--ink)}
.card-info .who{font-size:6.5px;font-weight:700;color:var(--brown)}
.card-rule{position:absolute;left:0;right:0;bottom:0;height:12px;background:var(--brown);font-size:4.5px;color:var(--orange);text-align:center;line-height:12px;letter-spacing:.2em;text-transform:uppercase}
.card-back{top:786px;background:var(--brown)}
.card-back .brand{position:absolute;inset:0;justify-content:center}
.card-back .brand-dot{width:30px;height:30px}
.card-back .brand-name{font-size:7px;color:var(--orange)}

/* envelopes */
.env-front{left:217px;top:671px;width:434px;height:222px;overflow:hidden}
.env-front .brand{position:absolute;left:22px;top:18px;flex-direction:column;gap:4px;width:80px}
.env-front .brand-dot{width:36px;height:36px}
.env-front .brand-name{font-size:6.5px;color:var(--brown);text-align:center}
.env-address{position:absolute;left:22px;top:92px;font-size:5px;line-height:1.7;color:var(--muted)}
.env-ghost{position:absolute;left:170px;top:36px;width:150px;height:150px;border-radius:50%;background:var(--ghost)}
.env-back{left:669px;top:671px;width:475px;height:222px}
.env-back svg{position:absolute;inset:0}
.env-back-web{position:absolute;left:0;right:0;top:18px;text-align:center;font-size:6px;letter-spacing:.28em;color:var(--brown);text-transform:uppercase}
</style>
</head>
<body>

<section class="sheet letterhead">
  <div class="brand"><span class="brand-dot"></span><span class="brand-name">Ridgepath<br>Outfitters</span></div>
  <div class="lh-contact">Garrick Fenn<br>27615 Marrow Lane Victorville, CA 92307<br>garrickfenn@mailbrook.com<br>www.ridgepathoutfitters.com</div>
  <div class="lh-body">
    <p>June 12, 2024</p>
    <p>Client Name<br>Street Address, City</p>
    <p>Dear Guest,</p>
    <p>Thank you for choosing us for your next climb in the high desert. Our guides will meet you at the trailhead with all gear ready and a clear plan for the day.</p>
    <p>Please bring water, sun cover and sturdy shoes. We will send a short checklist one week before your trip.</p>
    <p>We look forward to a safe and memorable day on the rock with you and your group.</p>
    <p>Best Regards,</p>
    <div class="lh-sign"></div>
    <p>Garrick Fenn<br>Director</p>
  </div>
  <div class="lh-footer">www.ridgepathoutfitters.com</div>
</section>

<section class="sheet folder">
  <div class="brand"><span class="brand-dot"></span><span class="brand-name">Ridgepath Outfitters</span></div>
  <div class="folder-web">www.ridgepathoutfitters.com</div>
</section>

<section class="sheet card card-front">
  <div class="brand"><span class="brand-dot"></span><span class="brand-name">Ridgepath<br>Outfitters</span></div>
  <div class="card-info">
    <div class="who">Garrick Fenn</div>
    Director<br>27615 Marrow Lane<br>Victorville, CA 92307<br>garrickfenn@mailbrook.com
  </div>
  <div class="card-rule">www.ridgepathoutfitters.com</div>
</section>

<section class="sheet card card-back">
  <div class="brand"><span class="brand-dot"></span><span class="brand-name">Ridgepath Outfitters</span></div>
</section>

<section class="sheet env-front">
  <div class="env-ghost" aria-hidden="true"></div>
  <div class="brand"><span class="brand-dot"></span><span class="brand-name">Ridgepath<br>Outfitters</span></div>
  <div class="env-address">27615 Marrow Lane<br>Victorville, CA 92307</div>
</section>

<section class="sheet env-back">
  <svg width="475" height="222" viewBox="0 0 475 222" aria-hidden="true">
    <polyline points="0,0 237.5,120 475,0" fill="none" stroke="#dcd9d6" stroke-width="1"/>
  </svg>
  <div class="env-back-web">www.ridgepathoutfitters.com</div>
</section>

</body>
</html>
```